Dental Business Card Design w/logo

Classic, elegant w/a touch of contemporary
Upscale dental facility located in Modesto CA
Specializing in restorative & general dentistry
Providing exceptional customer service to the community
Updates

I prefer script and not bold writing
If you can use the phone; fax and email icons instead of spelling them out, it would be great
No bold colors
Classy and elegant
In the back of the card I would like to see something like this
Your Next Appointment:
Mon     Tue    Wed    Thur (a box next to each of them for marking)
Date:_______________ at_____________ AM    PM  (a box next to them for marking)

Thank you

Target Market(s)

Well established professional

Industry/Entity Type

Dental

Contact Information for Business Card

Velorine Tamsuki DMD
4176 Larchmont Rd
Suite D7
Modesto, CA 95368

Office: 209-731-5092
Fax: 209-731-8247
Email: tamsukidmd@brivelmail.test

Requirements
Must have
• Unique classic logo
An easily repeatable design that can be used on letterhead and envelopes
Nice to have
• My initials incorporated into unique design
Should not have
• No cartoons or cheesy themes. This is a practice for the well established and professional individual.

```html
<!DOCTYPE html>
<html lang="en">
<head>
<meta charset="utf-8">
<title>Larchmont Dental — Business Card</title>
<link rel="stylesheet" href="https://fonts.googleapis.com/css2?family=Mulish:wght@400;800&display=swap">
<style>
  :root {
    --brand-blue: #199fd9;
    --paper: #ffffff;
    --stone: #cfd0d2;
    --stone-dark: #bfc0c2;
    --ice: #c6e8f3;
    --backdrop: #eceae6;
  }
  * { box-sizing: border-box; margin: 0; padding: 0; }
  html, body { width: 1200px; height: 1000px; overflow: hidden; }
  body {
    background: var(--backdrop);
    font-family: "Mulish", "Century Gothic", sans-serif;
    position: relative;
  }
  .card {
    position: absolute;
    width: 700px;
    height: 400px;
    border-radius: 28px;
    overflow: hidden;
    box-shadow: 0 10px 28px rgba(0,0,0,.18);
  }

  /* Front */
  .card-front { left: 150px; top: 60px; background: var(--brand-blue); }
  .front-brand {
    position: absolute; left: 0; right: 0; top: 118px;
    display: flex; align-items: center; justify-content: center; gap: 18px;
  }
  .brand-dot { width: 30px; height: 30px; border-radius: 50%; background: var(--ice); }
  .brand-name {
    font-weight: 800; color: var(--stone); font-size: 52px; letter-spacing: 1px;
  }
  .tagline-band {
    position: absolute; left: 0; right: 0; top: 300px; height: 50px;
    background: var(--paper);
    display: flex; align-items: center; justify-content: center;
  }
  .tagline { color: var(--brand-blue); font-size: 21px; font-weight: 400; }

  /* Back */
  .card-back { left: 350px; top: 540px; background: var(--paper); }
  .back-brand {
    position: absolute; right: 34px; top: 30px;
    display: flex; align-items: center; gap: 10px;
  }
  .back-brand .brand-dot { width: 18px; height: 18px; }
  .back-brand .brand-name { font-size: 30px; }
  .practitioner {
    position: absolute; left: 40px; top: 96px;
    font-weight: 800; color: var(--stone); font-size: 31px;
  }
  .divider { position: absolute; left: 0; right: 0; top: 144px; height: 8px; background: var(--stone-dark); }
  .contact-panel {
    position: absolute; left: 0; right: 0; top: 152px; bottom: 0;
    background: var(--brand-blue); color: var(--paper);
  }
  .contact-list { position: absolute; left: 38px; top: 40px; list-style: none; }
  .contact-list li {
    display: flex; align-items: center; gap: 10px;
    font-size: 26px; line-height: 40px;
  }
  .contact-list svg { width: 22px; height: 22px; flex: none; }
  .address {
    position: absolute; right: 40px; top: 100px; text-align: right;
    font-size: 26px; line-height: 36px; font-style: normal;
  }
</style>
</head>
<body>
  <section class="card card-front">
    <div class="front-brand">
      <span class="brand-dot"></span>
      <span class="brand-name">Larchmont Dental</span>
    </div>
    <div class="tagline-band">
      <p class="tagline">Specializing in restorative &amp; general dentistry</p>
    </div>
  </section>

  <section class="card card-back">
    <div class="back-brand">
      <span class="brand-dot"></span>
      <span class="brand-name">Larchmont Dental</span>
    </div>
    <h1 class="practitioner">Velorine Tamsuki DMD</h1>
    <div class="divider"></div>
    <div class="contact-panel">
      <ul class="contact-list">
        <li>
          <svg viewBox="0 0 24 24" aria-label="Phone"><path fill="#fff" d="M6.6 2.5l3 3.2-1.8 2.6c1 2.4 3.4 4.9 5.9 6l2.6-1.8 3.2 3-1.6 3.4C11 19.4 4.6 13 3.2 4.1z"/></svg>
          <span>209-731-5092</span>
        </li>
        <li>
          <svg viewBox="0 0 24 24" aria-label="Fax"><g fill="none" stroke="#fff" stroke-width="1.8"><rect x="6" y="2" width="12" height="7"/><rect x="2.5" y="9" width="19" height="10" rx="1.5"/><line x1="6" y1="14" x2="18" y2="14"/></g></svg>
          <span>209-731-8247</span>
        </li>
        <li>
          <svg viewBox="0 0 24 24" aria-label="Email"><g fill="none" stroke="#fff" stroke-width="1.8"><rect x="2" y="5" width="20" height="14"/><polyline points="2,5 12,13 22,5"/></g></svg>
          <span>tamsukidmd@brivelmail.test</span>
        </li>
      </ul>
      <address class="address">
        4176 Larchmont Rd<br>
        Suite D7 Modesto<br>
        CA 95368
      </address>
    </div>
  </section>
</body>
</html>
```